Brightmoor Pathways

We need a website designed for a life coaching company who specialises in one on one coaching, workshops and seminars where they teach participants in goal setting and how to achieve them for a better life.

Objectives

·         Easy to use

·         Clear & concise

·         Quality but not too flashy

·         Shows clearly what you do and how you interact with clients

·         No fuss, straight up

·         Gives those who hear your name or business name a place to go to obtain further information on what I am doing, why & how they can use my services.

·         A way for clients to contact you

·         Seminar & workshop bookings (not mandatory)

·         Most of the website to be static.

Number of Pages Required

1 page

Requirements
Must have
• Sitemap

• Home
• About Us
• One on One Coaching
• Workshops/Seminars
• How we Work?
• Pricing
• Testimonials
• Contact Us

• Design/Content Brief

• ü  The following elements are included in the design/content brief which this proposal is based on:

• o    Flash banner with some images rotating that reflect your business.

• o    Logo and phone number 0438 760 214 will be prominently displayed.

• o    Horizontal Navigation

• o    Contact Us icon on homepage

• o    Sign up for our newsletter on homepage

• o    Privacy Policy/Sitemap/Terms & Conditions in footer

• o    - larger rounded buttons

• o    - good size font

• o    - not having to scroll too far

• o    - soft feel, but not fluffy (images will enhance this)

• ü  Colours that could be used with logo

• o   What about this?  RGB 128,128,128

• o   What about this?  RGB 54, 95, 145

• o   What about this?  RGB 51, 204, 51

• o   Red – R255

• ü   http://www.plumvexlo.com/

• o    I like this website and its rounded buttons, large easy to see and use.

• o    Soft colours

• o    Changing pictures at the top of screen

• Files

```html
<!DOCTYPE html>
<html lang="en">
<head>
<meta charset="utf-8">
<title>Brightmoor Pathways – Life Coaching</title>
<link rel="stylesheet" href="https://fonts.googleapis.com/css2?family=Cabin:wght@400;600;700&display=swap">
<style>
  :root {
    --sky-top: #eaf3fb;
    --sky-bottom: #b9d9f3;
    --panel: #ffffff;
    --panel-fade: #e6f1fa;
    --green-light: #a6dc3c;
    --green: #7cc31f;
    --green-dark: #5fa515;
    --blue: #2e8fd9;
    --blue-button-top: #5fb4ef;
    --blue-button-bottom: #2a86d3;
    --banner-top: #8fbde6;
    --banner-bottom: #b7d6ee;
    --red: #d9331c;
    --ink: #404040;
    --ink-soft: #555555;
    --white: #ffffff;
  }
  * { box-sizing: border-box; margin: 0; padding: 0; }
  html, body { width: 1200px; height: 900px; overflow: hidden; }
  body {
    position: relative;
    font-family: "Cabin", "Gill Sans", sans-serif;
    color: var(--ink);
    background: linear-gradient(to bottom, var(--sky-top), var(--sky-bottom));
  }
  .page {
    position: absolute; left: 75px; top: 73px; width: 1055px; height: 730px;
    background: linear-gradient(to bottom, var(--panel) 0%, var(--panel) 45%, var(--panel-fade) 100%);
  }
  .brand {
    position: absolute; left: 36px; top: 44px;
    display: flex; align-items: center; gap: 12px;
    font-size: 30px; font-weight: 600; color: var(--ink);
  }
  .brand-square { width: 22px; height: 22px; background: var(--green); }
  .call { position: absolute; right: 42px; top: 47px; text-align: right; }
  .call-label { font-size: 18px; color: var(--blue); letter-spacing: -0.2px; }
  .call-number { font-size: 18px; font-weight: 700; color: var(--ink); letter-spacing: 1px; margin-top: 5px; }
  .main-nav {
    position: absolute; left: 29px; top: 121px; width: 996px; height: 45px;
    display: flex; border-radius: 10px 10px 0 0;
    background: linear-gradient(to bottom, var(--green-light), var(--green));
  }
  .main-nav a {
    display: flex; align-items: center; justify-content: center;
    color: var(--white); text-decoration: none; font-size: 17.5px;
    border-left: 1px solid rgba(255,255,255,0.35);
  }
  .main-nav a:first-child { border-left: none; }
  .banner {
    position: absolute; left: 29px; top: 166px; width: 996px; height: 232px;
    background: linear-gradient(to bottom, var(--banner-top), var(--banner-bottom));
  }
  .signup {
    position: absolute; left: 29px; top: 438px; width: 235px; height: 235px;
    border-radius: 16px; text-align: center;
    background: linear-gradient(to bottom, #e3f3c6 0%, var(--green-light) 60%, var(--green) 100%);
    border: 1px solid var(--green-dark);
  }
  .signup-text { margin-top: 27px; font-size: 15.5px; line-height: 22px; color: var(--ink-soft); }
  .signup-text strong { color: var(--red); font-weight: 700; }
  .signup-email {
    display: block; margin: 20px auto 0; width: 196px; height: 27px;
    border: 1px solid #888; background: var(--white);
    font-family: inherit; font-size: 15px; color: var(--ink-soft); padding: 0 4px;
  }
  .signup-button {
    display: block; margin: 12px auto 0; width: 194px; height: 33px;
    border: none; border-radius: 14px; color: var(--white);
    font-family: inherit; font-size: 18px;
    background: linear-gradient(to bottom, var(--blue-button-top), var(--blue-button-bottom));
  }
  .intro { position: absolute; left: 292px; top: 432px; width: 712px; }
  .intro h1 { font-size: 29px; font-weight: 400; color: var(--blue); line-height: 36px; }
  .intro p { font-size: 17px; line-height: 26px; color: var(--ink-soft); margin-bottom: 26px; }
  .site-footer {
    position: absolute; left: 0; top: 823px; width: 1200px;
    display: flex; justify-content: center; gap: 32px;
    font-size: 13.5px; color: var(--ink);
  }
  .site-footer a { color: var(--ink); text-decoration: none; }
</style>
</head>
<body>
  <div class="page">
    <header>
      <div class="brand"><span class="brand-square"></span>Brightmoor Pathways</div>
      <div class="call">
        <div class="call-label">Call Us Today:</div>
        <div class="call-number">0438 760 214</div>
      </div>
    </header>
    <nav class="main-nav">
      <a href="#" style="width:81px">Home</a>
      <a href="#" style="width:93px">About Us</a>
      <a href="#" style="width:199px">One-On-One Coaching</a>
      <a href="#" style="width:182px">Workshops/Seminars</a>
      <a href="#" style="width:137px">How we work?</a>
      <a href="#" style="width:70px">Pricing</a>
      <a href="#" style="width:112px">Testimonials</a>
      <a href="#" style="width:122px">Contact Us</a>
    </nav>
    <div class="banner" role="img" aria-label="Rotating banner photos: a hurdler leaping and a group of people jumping for joy outdoors"></div>
    <aside class="signup">
      <p class="signup-text">Sign up to receive our<br><strong>Brightmoor Pathways</strong><br>newsletter with special<br>offers, news and helpful tips!</p>
      <input class="signup-email" type="text" value="your email address here" aria-label="Email address">
      <button class="signup-button">SIGN UP!</button>
    </aside>
    <main class="intro">
      <h1>Brightmoor Pathways</h1>
      <p>Rud minit aute dolutatio el ut volobor sit nit ut verostrud esequi tatuerosto dolortis am, core feummy non vent augait aute dolobore modionsectem zzriustrud tat, sisit ametummy nulla atueros nim iustio enibh er sum erciliq uationsenisl eum venit at. Ut utat, quis aliquat, volobor tionse molute feu facil et augiamcoreet veniamet la feugiamet at ullut am ero coreetumsan ea alismolortis nulla conullum eum do conulput la at lamet, quat.</p>
      <p>Diat. Luptat adigniam dolore consecte commy nisim num dolorem iril ulput lan ulputatie commodio odipsusci er secte mincidunt utpat.</p>
    </main>
  </div>
  <footer class="site-footer">
    <span>©2009 Brightmoor Pathways</span>
    <a href="#">Contact Us</a>
    <a href="#">Privacy Policy</a>
    <a href="#">Sitemap</a>
    <a href="#">Terms &amp; Conditions</a>
  </footer>
</body>
</html>
```